New Company Business Card design

Looking for a corporate looking business card utilising my new logo design - the logo i would like embossed as one option and flat as another - simplistic but stylish - less is more - we are an import export business launching into the market - i would like a couple of options as main background - Grey or Black

```html
<!DOCTYPE html>
<html lang="en">
<head>
<meta charset="utf-8">
<title>Harborline Trade Solutions – Business Cards</title>
<link href="https://fonts.googleapis.com/css2?family=Barlow:wght@400;500;600&display=swap" rel="stylesheet">
<style>
  :root {
    --stage: #43fd3b;
    --paper: #f3f4f2;
    --ink-dark: #13181a;
    --strip: #1c2326;
    --brand-blue: #2a7fe6;
    --text-grey: #56626a;
    --text-dark: #2c3438;
    --rule: #9fd2c4;
    --rule-dark: #3a4448;
  }
  * { box-sizing: border-box; margin: 0; padding: 0; }
  html, body { width: 1200px; height: 1200px; overflow: hidden; }
  body {
    background: var(--stage);
    font-family: "Barlow", Arial, sans-serif;
    position: relative;
  }
  .card {
    position: absolute;
    width: 516px;
    height: 310px;
    background: var(--paper);
  }
  .card--front-light { left: 58px; top: 266px; }
  .card--front-dark  { left: 58px; top: 634px; background: var(--ink-dark); }
  .card--back-plain  { left: 653px; top: 266px; }
  .card--back-brand  { left: 653px; top: 634px; }

  /* Front: company name */
  .brand-lockup {
    position: absolute;
    left: 0; right: 0; top: 112px;
    text-align: center;
  }
  .brand-name {
    font-weight: 600;
    font-size: 27px;
    letter-spacing: 1px;
    color: var(--brand-blue);
    display: inline-flex;
    align-items: center;
    gap: 10px;
  }
  .brand-dot {
    width: 16px; height: 16px; border-radius: 50%;
    background: var(--brand-blue);
  }
  .brand-tagline {
    margin-top: 14px;
    font-size: 10px;
    letter-spacing: 3.2px;
    text-transform: uppercase;
    color: var(--text-grey);
  }
  .card--front-dark .brand-tagline { color: #4d565b; }

  /* Back */
  .side-strip {
    position: absolute; left: 0; top: 0; bottom: 0;
    width: 47px;
    background: var(--strip);
  }
  .holder {
    position: absolute; left: 0; top: 53px;
    display: flex; align-items: flex-start;
  }
  .holder-icon { width: 47px; display: flex; justify-content: center; padding-top: 2px; }
  .holder-name {
    font-weight: 600; font-size: 21px; color: var(--text-grey);
    letter-spacing: 0.3px; line-height: 1.1; padding-left: 8px;
  }
  .holder-title {
    font-size: 13px; color: var(--text-dark); margin-top: 5px; padding-left: 8px;
    letter-spacing: 0.3px;
  }
  .contact-list {
    position: absolute; left: 0; top: 157px; list-style: none;
  }
  .contact-item {
    display: flex; align-items: center; height: 21px;
  }
  .contact-icon {
    width: 47px; height: 21px;
    display: flex; align-items: center; justify-content: center;
    border-top: 1px solid var(--rule-dark);
  }
  .contact-text {
    font-size: 12.2px; color: var(--text-dark); letter-spacing: 0.3px;
    padding: 0 8px;
    margin-left: 1px;
    height: 21px; line-height: 21px;
    border-bottom: 1px solid var(--rule);
  }
  .contact-item:last-child .contact-icon { border-bottom: 1px solid var(--rule-dark); }
  .contact-item:nth-child(1) .contact-text,
  .contact-item:nth-child(2) .contact-text { min-width: 192px; }
  .contact-item:nth-child(3) .contact-text { min-width: 192px; }

  .back-mark {
    position: absolute; right: 58px; top: 112px;
    display: flex; align-items: center; gap: 10px;
    font-weight: 600; font-size: 30px; color: var(--brand-blue);
  }
  .back-mark .brand-dot { width: 18px; height: 18px; opacity: 0.25; }
</style>
</head>
<body>

<section class="card card--front-light">
  <div class="brand-lockup">
    <div class="brand-name"><span class="brand-dot"></span>HARBORLINE TRADE SOLUTIONS</div>
    <p class="brand-tagline">Global sourcing to meet local needs</p>
  </div>
</section>

<section class="card card--front-dark">
  <div class="brand-lockup">
    <div class="brand-name"><span class="brand-dot"></span>HARBORLINE TRADE SOLUTIONS</div>
    <p class="brand-tagline">Global sourcing to meet local needs</p>
  </div>
</section>

<section class="card card--back-plain">
  <div class="side-strip"></div>
  <div class="holder">
    <div class="holder-icon">
      <svg width="24" height="24" viewBox="0 0 24 24"><circle cx="12" cy="7" r="5" fill="#fff"/><path d="M2 23c0-6 4.5-9 10-9s10 3 10 9z" fill="#fff"/></svg>
    </div>
    <div>
      <p class="holder-name">Dr. Daniel Okafor</p>
      <p class="holder-title">Teaching Pastor</p>
    </div>
  </div>
  <ul class="contact-list">
    <li class="contact-item"><span class="contact-icon"><svg width="11" height="11" viewBox="0 0 24 24"><path d="M6 2l4 5-2.5 2.5a13 13 0 0 0 7 7L17 14l5 4-2 4C11 22 2 13 2 4z" fill="#fff"/></svg></span><span class="contact-text">5550143278</span></li>
    <li class="contact-item"><span class="contact-icon"><svg width="10" height="8" viewBox="0 0 20 14"><rect width="20" height="14" fill="#fff"/><path d="M0 0l10 8 10-8" stroke="#1c2326" stroke-width="2" fill="none"/></svg></span><span class="contact-text">dokafor@harborlinetrade.com</span></li>
    <li class="contact-item"><span class="contact-icon"><svg width="11" height="11" viewBox="0 0 24 24" fill="none" stroke="#fff" stroke-width="2"><circle cx="12" cy="12" r="10"/><ellipse cx="12" cy="12" rx="4" ry="10"/><path d="M2 12h20M4 6h16M4 18h16"/></svg></span><span class="contact-text">www.harborlinetrade.com</span></li>
    <li class="contact-item"><span class="contact-icon"><svg width="9" height="12" viewBox="0 0 18 24"><path d="M9 0a9 9 0 0 1 9 9c0 6-9 15-9 15S0 15 0 9a9 9 0 0 1 9-9z" fill="#fff"/><circle cx="9" cy="9" r="3.5" fill="#1c2326"/></svg></span><span class="contact-text">418 N Maple Avenue Fairview, OR 97024</span></li>
  </ul>
</section>

<section class="card card--back-brand">
  <div class="side-strip"></div>
  <div class="holder">
    <div class="holder-icon">
      <svg width="24" height="24" viewBox="0 0 24 24"><circle cx="12" cy="7" r="5" fill="#fff"/><path d="M2 23c0-6 4.5-9 10-9s10 3 10 9z" fill="#fff"/></svg>
    </div>
    <div>
      <p class="holder-name">Dr. Daniel Okafor</p>
      <p class="holder-title">Teaching Pastor</p>
    </div>
  </div>
  <div class="back-mark"><span class="brand-dot"></span>HARBORLINE</div>
  <ul class="contact-list">
    <li class="contact-item"><span class="contact-icon"><svg width="11" height="11" viewBox="0 0 24 24"><path d="M6 2l4 5-2.5 2.5a13 13 0 0 0 7 7L17 14l5 4-2 4C11 22 2 13 2 4z" fill="#fff"/></svg></span><span class="contact-text">5550143278</span></li>
    <li class="contact-item"><span class="contact-icon"><svg width="10" height="8" viewBox="0 0 20 14"><rect width="20" height="14" fill="#fff"/><path d="M0 0l10 8 10-8" stroke="#1c2326" stroke-width="2" fill="none"/></svg></span><span class="contact-text">dokafor@harborlinetrade.com</span></li>
    <li class="contact-item"><span class="contact-icon"><svg width="11" height="11" viewBox="0 0 24 24" fill="none" stroke="#fff" stroke-width="2"><circle cx="12" cy="12" r="10"/><ellipse cx="12" cy="12" rx="4" ry="10"/><path d="M2 12h20M4 6h16M4 18h16"/></svg></span><span class="contact-text">www.harborlinetrade.com</span></li>
    <li class="contact-item"><span class="contact-icon"><svg width="9" height="12" viewBox="0 0 18 24"><path d="M9 0a9 9 0 0 1 9 9c0 6-9 15-9 15S0 15 0 9a9 9 0 0 1 9-9z" fill="#fff"/><circle cx="9" cy="9" r="3.5" fill="#1c2326"/></svg></span><span class="contact-text">418 N Maple Avenue Fairview, OR 97024</span></li>
  </ul>
</section>

</body>
</html>
```